Marisa Dunwell writer

I need a design for my business cards I write verses quotes and put them on to canvas, for children adults.
I like the idea of a quill pen and I love colour and a bit of magic as words can be magical.
My email address is tornbek@mailvara.example PH: 0400817362
Here is an example of what I write
Can you put this verse on it
WORDS
Words can bring a tear to the eye
Words can make a heart sigh
Words can colour a world thats bland
Words can help one understand

This one is just a sample of my type of writing to give you an idea of the feel i'm looking for.
You'r Freind
I promise to be there
When life seems unfair
Sit with you when you cry
Wiping that tear from your eye
Holding you through the pain
Until you smile again
On me you can depend
Always your friend
Marisa Dunwell (c)

Target Market(s)

My target market is everyone family friend lover .

Industry/Entity Type

Business

Colors

Designer to choose colors to be used in the design.

```html
<!DOCTYPE html>
<html lang="en">
<head>
<meta charset="utf-8">
<title>Marisa Dunwell – Business Cards</title>
<link rel="stylesheet" href="https://fonts.googleapis.com/css2?family=Lora:wght@400;500&family=Courgette&display=swap">
<style>
  :root {
    --backdrop: #ece9e4;
    --card-stock: #edebe5;
    --ink-teal: #2f6b72;
    --turquoise: #86d6d2;
    --turquoise-deep: #6cc3bf;
    --ink-white: #fbfdfc;
    --flourish: #c8ecea;
  }
  * { box-sizing: border-box; margin: 0; padding: 0; }
  html, body { width: 1200px; height: 1000px; overflow: hidden; }
  body { background: var(--backdrop); position: relative; font-family: "Lora", serif; }

  .card {
    position: absolute;
    left: 250px;
    width: 700px;
    height: 400px;
    border-radius: 4px;
    box-shadow: 0 6px 18px rgba(0,0,0,0.12);
  }

  /* Front */
  .card--front { top: 60px; background: var(--card-stock); color: var(--ink-teal); }
  .front-brand {
    position: absolute; left: 0; right: 0; top: 130px;
    display: flex; align-items: center; justify-content: center; gap: 22px;
  }
  .brand-dot { width: 26px; height: 26px; border-radius: 50%; background: var(--ink-teal); }
  .front-name { font-size: 64px; font-weight: 500; letter-spacing: 1px; }
  .front-tagline {
    position: absolute; left: 0; right: 0; top: 240px; text-align: center;
    font-family: "Courgette", cursive; font-size: 24px; letter-spacing: 2px;
  }

  /* Back */
  .card--back { top: 540px; background: var(--turquoise); color: var(--ink-white); }
  .back-brand {
    position: absolute; left: 40px; top: 60px; width: 360px;
    display: flex; align-items: center; gap: 14px;
    padding-bottom: 10px; border-bottom: 2px solid var(--ink-white);
  }
  .back-brand .brand-dot { width: 18px; height: 18px; background: var(--ink-white); }
  .back-name { font-size: 40px; font-weight: 500; }

  .contact { position: absolute; left: 40px; top: 230px; }
  .contact-name { font-family: "Courgette", cursive; font-size: 26px; margin-bottom: 14px; }
  .contact-line { font-size: 17px; line-height: 1.35; }

  .offer {
    position: absolute; right: 40px; top: 50px; width: 240px; text-align: center; line-height: 1.1;
  }
  .offer-script { font-family: "Courgette", cursive; font-size: 26px; }
  .offer-caps { font-size: 28px; letter-spacing: 1px; }
  .offer-you { font-family: "Courgette", cursive; font-size: 52px; }

  .flourish {
    position: absolute; left: 330px; top: 300px; width: 330px; height: 70px;
    border-radius: 35px;
    background: linear-gradient(90deg, var(--turquoise), var(--flourish) 50%, var(--turquoise));
  }
</style>
</head>
<body>
  <section class="card card--front">
    <div class="front-brand">
      <span class="brand-dot"></span>
      <span class="front-name">Marisa Dunwell</span>
    </div>
    <p class="front-tagline">writer · poet · artist</p>
  </section>

  <section class="card card--back">
    <div class="back-brand">
      <span class="brand-dot"></span>
      <span class="back-name">Marisa Dunwell</span>
    </div>

    <div class="contact">
      <p class="contact-name">Marisa Dunwell</p>
      <p class="contact-line">tornbek@mailvara.example</p>
      <p class="contact-line">0400817362</p>
      <p class="contact-line">marisadunwell.example</p>
    </div>

    <div class="offer">
      <p class="offer-script">verses &amp; quotes</p>
      <p class="offer-caps">ON CANVAS</p>
      <p class="offer-script">specially made</p>
      <p class="offer-caps">FOR</p>
      <p class="offer-you">You</p>
    </div>

    <div class="flourish" role="img" aria-label="Decorative white floral scroll ornament"></div>
  </section>
</body>
</html>
```